Marketing Concept Needed - Do It Yourself Multi-Purpose Stand Alone Room

I need a marketing/advertising piece that will sell my concept to the end user. The idea is that someone who needs some extra space or private space or office space or storage space or guest room space or garden space or kids play room space, ETC can purchase my do it yourself stand alone room, which is also environmentally friendly. This is a standalone structure in the backyard or back lot that someone can have some "me time" in for whatever they need it for.

I have attached some thoughts for this concept but none jump out at me yet. The product is very environmentally friendly, but I am not sure that is the ‘grabber’. The end user buys the shell from me and then finishes it in any way they want. Most will probably match it to their existing home or structure (brick, vinyl siding, shingles, stone, whatever). I sell the room shell which is the floor, walls and sub-roof and they finish it the way they want.

I think this is an impulse buy. For example, for $2995 you can have your own 100 SF room finished to your taste and liking. 100 SF is the standard size but the unit can be customized for the size the end user needs.

The Larkspire Room (or whatever we call it) installs in just two days with two people. Or our staff will install it for you. Not sure what to do with photos but my thought is that we could show the basic shell with no siding on it and then pictures of various finishes and colors that they can use to complete the room (see photos is separate file).

We could include a few drawings of various furniture layouts.

What is the grabber? Do it yourself, green, price, speed of installation, ETC.

What is the best way to convey the message (copy, photos, sketches/renderings)? We could use some stock photos of family playing, person working, someone gardening, storing, etc.

We can include some stock photos

This project includes writing the copy for the piece.

Tag line, product name (Stand Alone Do It Yourself Eco Multi Purpose Room.......obviously needs to be more concise than this).

Target Market(s)

I think the end user is a guy or girl that needs some space for themselves (think mancave, but that is too over used). I think the age range would be 30 to 60 years of age.

Someone who needs some 'me' space for some 'me' time.

Someone who needs an extra room but cannot afford to expand their existing house or building or has no room to do so.

Could target folks who are starting a business and needs a small office.

Industry/Entity Type

Marketing

Requirements
Must have
• Not sure about this. Do it yourself. Green/Eco Friendly. Fast. Cost Effective Space.

I am very open to what we include and don't include. Just need something concise and to the point that sells the concept.

```html
<!DOCTYPE html>
<html lang="en">
<head>
<meta charset="utf-8">
<title>Larkspire Room — Time and Space for Doing Your Thing</title>
<link rel="stylesheet" href="https://fonts.googleapis.com/css2?family=EB+Garamond:wght@400;500&family=Open+Sans:ital,wght@1,700&display=swap">
<style>
  :root {
    --maroon: #7a4543;
    --maroon-deep: #5b2d2c;
    --maroon-edge: #4e2524;
    --ink-light: #ffffff;
    --ink-muted: #b38d89;
    --ink-footer: #a8918f;
    --gap: #f3efe9;
    --pottery: linear-gradient(160deg, #d9cdbb 0%, #a89276 55%, #6d5a44 100%);
    --glass: linear-gradient(160deg, #e6ded2 0%, #b9a18a 50%, #7c5f4a 100%);
    --artist: linear-gradient(160deg, #e8e6e2 0%, #a9a39c 50%, #4a3e38 100%);
    --music: linear-gradient(160deg, #cfc6bb 0%, #6e5d52 50%, #2f2a2a 100%);
  }
  * { margin: 0; padding: 0; box-sizing: border-box; }
  html, body { width: 927px; height: 1200px; overflow: hidden; background: var(--maroon); }
  .poster {
    position: relative;
    width: 927px;
    height: 1200px;
    background: var(--maroon);
    font-family: "EB Garamond", Garamond, serif;
    color: var(--ink-light);
    overflow: hidden;
  }
  .poster__topline {
    position: absolute; left: 0; top: 0; width: 100%; height: 10px;
    background: var(--maroon-deep);
  }
  .headline__line {
    position: absolute; left: 0; width: 100%;
    display: flex; justify-content: center; align-items: baseline;
    line-height: 1; white-space: pre;
  }
  .headline__line--one { top: 56px; }
  .headline__line--two { top: 126px; }
  .headline__line--three { top: 248px; }
  .size-caps { font-size: 76px; }
  .size-small { font-size: 56px; }
  .size-mid { font-size: 60px; }
  .size-big { font-size: 116px; }

  .gallery {
    position: absolute; left: 0; top: 416px; width: 927px; height: 355px;
    background: var(--gap);
  }
  .gallery__photo { position: absolute; top: 0; height: 355px; }
  .gallery__photo--pottery { left: 0; width: 223px; background: var(--pottery); }
  .gallery__photo--glass { left: 229px; width: 232px; background: var(--glass); }
  .gallery__photo--artist { left: 467px; width: 230px; background: var(--artist); }
  .gallery__photo--music { left: 704px; width: 223px; background: var(--music); }

  .activities {
    position: absolute; left: 0; width: 100%; text-align: center;
    font-size: 40px; line-height: 1; color: var(--ink-muted);
  }
  .activities--one { top: 808px; }
  .activities--two { top: 880px; }
  .closer {
    position: absolute; left: 0; top: 950px; width: 100%; text-align: center;
    font-size: 78px; line-height: 1; color: var(--ink-light);
  }
  .footer {
    position: absolute; left: 0; top: 1060px; width: 100%; height: 140px;
    background: var(--maroon-deep);
    border-top: 2px solid var(--maroon-edge);
    display: flex; flex-direction: column; align-items: center; justify-content: center;
    padding-bottom: 22px;
    font-family: "Open Sans", Arial, sans-serif;
    font-style: italic; font-weight: 700;
    font-size: 30px; line-height: 42px; color: var(--ink-footer);
  }
</style>
</head>
<body>
<main class="poster">
  <div class="poster__topline"></div>

  <h1 class="headline">
    <span class="headline__line headline__line--one"><span class="size-caps">NOW</span><span class="size-small"> there’s a</span></span>
    <span class="headline__line headline__line--two"><span class="size-big">time</span><span class="size-small"> and </span><span class="size-big">space</span></span>
    <span class="headline__line headline__line--three"><span class="size-mid">for doing </span><span class="size-big">your</span><span class="size-mid"> thing…</span></span>
  </h1>

  <section class="gallery">
    <div class="gallery__photo gallery__photo--pottery" role="img" aria-label="Woman shaping a clay pot on a pottery wheel in her studio"></div>
    <div class="gallery__photo gallery__photo--glass" role="img" aria-label="Older man working on stained glass at a workbench"></div>
    <div class="gallery__photo gallery__photo--artist" role="img" aria-label="Young woman relaxing in a chair beside jars of paintbrushes"></div>
    <div class="gallery__photo gallery__photo--music" role="img" aria-label="Man playing an electric guitar on a sofa"></div>
  </section>

  <p class="activities activities--one">…working…thinking…hobbies…playing</p>
  <p class="activities activities--two">…storing…reading…writing…studying…</p>
  <p class="closer">whatever it might be</p>

  <footer class="footer">
    <span>Eco-friendly, DYI construction</span>
    <span>- right in your own backyard</span>
  </footer>
</main>
</body>
</html>
```